Real Estate flyer for listing properties

This is a flyer to be used by the property lister (the person trying to convince property vendors to sell through us) of our real estate agency Golden Harbour (https://www.golden-harbour.example). The aim of the flyer is to convince owners to list their properties with us, so that we can advertise & sell them. We have our offices located in San Luis de Sabinillas / Manilva, Costa del Sol, Spain. The real estate market here is highly competetive and we want to stand out from our competition and establish trust, which is essential for owners to list with us.

I have attached the design of our old flyer. Please note that we would like the new flyer to use our new logo, and our colors, not the wine red color used previously

I have also added some photos of our offices and of properties we have sold. We can provide more photos on request.

1. Project Overview & Objectives
High-level goal: Convince owners in Manilva & nearby to list with us.

2. Style guidelines
Please stick with the current logo & Font. We do NOT require a logo re-design. The font for Golden Harbour is Myriad Pro Bold Italic in color #D1672E. The blue used is #65A8DE and yellow #F2E946
The flyer should be A5 size.

3. Mandatory elements
Section with agent photo, name, email address & phone number. The design should allow for the flyer to be two sided, where one side is in English, and the other side in Spanish.

4. Ideas
- Maybe include address of offices (Calle Los Pinos 8, 29601 San Luis de Sabinillas) or QR code to open on google
- Offer free valuations
- Maybe mention biggest portals we are on with logo e.g. Casaverde, Vivilar, Techos.example, Moravo, A Home By the Bay, etc
- List languages we speak (Spanish, English, German, Russian, Ukrainian, Lithuanian, French, Italian, Danish, Polish)
- We also offer: Maintenance & Key holding
- Mention we have clients waiting
Note, these are just ideas, obviously not everything can be on the flyer.

Please note that the final flyer should be good for printing, just to be updated with the agents picture and contact details. Meaning all the marketing text should be written.

5. Assets & Output
Output sizes: e.g. A5 print flyer (210 × 148 mm), plus a social-media optimized JPG (1080 × 1080 px).

File formats required: InDesign (editable), plus flattened PDF for print; JPG/PNG for web.

5. Additional task - "stationary"
We need a design for a flap folder. I have attached a photo of such a flap folder, as well as the illustrator printing guidelines from the printing company.

Feel free to message me in case you have any questions or doubts.

Industry/Entity Type

Real Estate

Requirements
Must have
• Use our company logo, color scheme (from logo)

```html
<!DOCTYPE html>
<html lang="en">
<head>
<meta charset="utf-8">
<title>Golden Harbour – Seller Flyer (EN / ES)</title>
<link href="https://fonts.googleapis.com/css2?family=Source+Sans+3:ital,wght@0,400;0,600;0,700;1,400&display=swap" rel="stylesheet">
<style>
  :root{
    --bg:#ECE7E1;
    --paper:#E7E4DF;
    --panel-grey:#D2CBC2;
    --panel-light:#DEDBD6;
    --yellow:#E0B232;
    --orange:#D1672E;
    --rust:#C0572B;
    --blue:#6FA2D6;
    --ink:#2B2A28;
    --muted:#5B5853;
  }
  *{box-sizing:border-box;margin:0;padding:0}
  html,body{width:1200px;height:1003px;overflow:hidden}
  body{background:var(--bg);font-family:"Source Sans 3",Arial,sans-serif;color:var(--ink);position:relative}

  .flyer{position:absolute;top:105px;width:560px;height:792px;background:var(--paper);overflow:hidden;box-shadow:0 2px 6px rgba(0,0,0,.12)}
  .flyer--en{left:30px}
  .flyer--es{left:610px}

  /* Hero panel */
  .hero{position:absolute;left:0;top:0;width:361px;height:350px;background:var(--panel-grey);border-bottom-right-radius:44px}
  .brand{position:absolute;left:48px;top:46px;display:flex;align-items:flex-start;gap:12px}
  .brand__mark{width:54px;height:54px;border-radius:50%;background:var(--yellow);flex:none;margin-top:4px}
  .brand__name{font-weight:700;font-size:27px;line-height:1;color:var(--orange)}
  .brand__areas{font-style:italic;font-size:13px;color:var(--muted);margin-top:5px}
  .brand__web{font-size:14.5px;color:var(--ink);margin-top:3px}

  .headline{position:absolute;left:0;right:0;top:142px;text-align:center;font-weight:700;line-height:1}
  .headline__line{display:block;font-size:43px;margin-bottom:4px;white-space:nowrap}
  .tag{display:inline-block;color:#fff;padding:0 4px;line-height:.98}
  .tag--blue{background:var(--blue)}
  .tag--yellow{background:var(--yellow)}
  .tag--rust{background:var(--rust)}
  .c-blue{color:var(--blue)}
  .c-yellow{color:var(--yellow)}
  .c-rust{color:var(--rust)}
  .hero__rule{position:absolute;left:140px;width:80px;height:2px;background:var(--ink)}
  .hero__cta{position:absolute;left:0;right:0;text-align:center;font-weight:700;font-size:17px}

  /* Agent panel */
  .agent{position:absolute;left:369px;top:0;width:191px;height:285px;background:var(--yellow)}
  .agent__title{position:absolute;right:18px;top:28px;text-align:right;font-weight:700;font-size:12px;line-height:1.3;text-transform:uppercase}
  .agent__photo{position:absolute;left:32px;top:99px;width:104px;height:104px;border-radius:50%;background:radial-gradient(circle at 50% 40%,#b98a6a 0 30%,#e9e3dc 62%)}
  .agent__hello{position:absolute;left:-33px;top:116px;width:73px;height:73px;border-radius:50%;background:var(--orange);color:#fff;font-weight:700;font-size:18px;display:flex;align-items:center;justify-content:center;transform:rotate(-14deg)}
  .agent__contact{position:absolute;left:0;right:0;top:210px;text-align:center;font-weight:700;font-size:12px;line-height:1.35}
  .agent__contact small{font-size:10.5px;font-weight:700}

  /* Photos */
  .photo{position:absolute}
  .photo--office{left:369px;top:293px;width:191px;height:139px;background:linear-gradient(180deg,#9fb6cc 0%,#c9a688 45%,#8c7a6c 100%)}
  .photo--building{left:0;top:358px;width:191px;height:434px;border-top-right-radius:40px;background:linear-gradient(180deg,#b9cfe6 0%,#e9e9e6 30%,#d6d6d2 70%,#7fb8df 88%,#4b9bd6 100%)}
  .photo--pool{left:199px;top:459px;width:162px;height:105px;border-radius:81px 81px 0 0;background:linear-gradient(180deg,#c7daee 0%,#e4e7ea 38%,#7da46c 55%,#5fa6d8 75%,#d9c9a8 100%)}

  /* Middle column */
  .question{position:absolute;left:199px;top:360px;width:162px;height:92px;border-radius:46px;background:var(--yellow);display:flex;align-items:center;justify-content:center;text-align:center;font-weight:700;font-size:17.5px;line-height:1.15;padding:0 10px}
  .offer{position:absolute;left:199px;top:564px;width:162px;height:228px;background:var(--yellow);text-align:center;padding:12px 8px 0}
  .offer__title{font-weight:700;font-size:18.5px;line-height:1.15}
  .offer__rule{width:46px;height:2px;background:var(--ink);margin:8px auto}
  .offer__contact{font-size:11.5px;line-height:1.4}
  .offer__text{font-size:11.5px;line-height:1.35}
  .offer__text strong{font-weight:700}

  /* Why panel */
  .why{position:absolute;left:369px;top:441px;width:191px;height:351px;background:var(--panel-light);border-top-left-radius:40px;padding:12px 8px 0 8px}
  .why__title{text-align:center;font-weight:700;font-size:27px;line-height:1.15;margin-bottom:8px}
  .flyer--es .why__title{font-size:19px;line-height:1.3;margin-bottom:10px}
  .why__list{list-style:none}
  .why__item{display:flex;align-items:flex-start;gap:8px;margin-bottom:8px;font-size:12px;line-height:1.3}
  .flyer--es .why__item{font-size:11px;margin-bottom:9px}
  .why__icon{flex:none;width:29px;height:29px;border-radius:50%;background:var(--yellow);display:flex;align-items:center;justify-content:center;margin-top:2px}
  .why__icon svg{width:16px;height:16px;stroke:var(--ink);fill:none;stroke-width:1.8;stroke-linecap:round;stroke-linejoin:round}
</style>
</head>
<body>

<!-- English side -->
<section class="flyer flyer--en" lang="en">
  <div class="hero">
    <div class="brand">
      <span class="brand__mark"></span>
      <div>
        <div class="brand__name">Golden Harbour</div>
        <div class="brand__areas">Marbella Estepona Sotogrande</div>
        <div class="brand__web">www.golden-harbour.example</div>
      </div>
    </div>
    <h1 class="headline">
      <span class="headline__line"><span class="tag tag--blue">Sell</span> <span class="c-blue">smart.</span></span>
      <span class="headline__line" style="padding-left:10px"><span class="tag tag--yellow">Sell</span> <span class="c-yellow">fast.</span></span>
      <span class="headline__line"><span class="tag tag--rust">Sell</span> <span class="c-rust">with us.</span></span>
    </h1>
    <div class="hero__rule" style="top:290px"></div>
    <p class="hero__cta" style="top:300px">Let’s get started today!</p>
  </div>

  <aside class="agent">
    <p class="agent__title">Your property<br>specialist for<br>Estepona, Manilva &amp;<br>Sotogrande</p>
    <div class="agent__hello">Hola!</div>
    <div class="agent__photo" role="img" aria-label="Portrait photo of the agent"></div>
    <p class="agent__contact">Lucia Marvel<br>(+34) 600 41 82 57<br><small>lucia@golden-harbour.example</small></p>
  </aside>

  <div class="photo photo--office" role="img" aria-label="Photo of the agency office on a street corner"></div>
  <div class="photo photo--building" role="img" aria-label="Photo of a white apartment building with a pool"></div>

  <h2 class="question">Selling Your Property on the Costa del Sol?</h2>
  <div class="photo photo--pool" role="img" aria-label="Photo of a residential complex with a pool"></div>
  <div class="offer">
    <h3 class="offer__title">We make it<br>easy, fast,<br>and profitable.</h3>
    <div class="offer__rule"></div>
    <p class="offer__contact">Call 951 000 742<br>sell@golden-harbour.example</p>
    <div class="offer__rule"></div>
    <p class="offer__text">We’ll come by, take professional photos, and provide a free valuation <strong>no strings attached.</strong></p>
  </div>

  <div class="why">
    <h2 class="why__title">Why Sell<br>With Us?</h2>
    <ul class="why__list">
      <li class="why__item"><span class="why__icon"><svg viewBox="0 0 16 16"><rect x="1.5" y="4.5" width="13" height="9" rx="1.5"/><circle cx="8" cy="9" r="2.5"/><path d="M5.5 4.5l1-2h3l1 2"/></svg></span>Stunning photos, drone shots &amp; 360° tours</li>
      <li class="why__item"><span class="why__icon"><svg viewBox="0 0 16 16"><rect x="1.5" y="2.5" width="8" height="7" rx="1"/><rect x="6.5" y="6.5" width="8" height="7" rx="1"/></svg></span>Multilingual descriptions &amp; top visibility</li>
      <li class="why__item"><span class="why__icon"><svg viewBox="0 0 16 16"><circle cx="7" cy="7" r="5"/><path d="M10.5 10.5l4 4"/><path d="M5 8V6.5l2-1.5 2 1.5V8z"/></svg></span>Listed with 2,000+ agencies + major portals</li>
      <li class="why__item"><span class="why__icon"><svg viewBox="0 0 16 16"><path d="M2 8l3-4 3 2 3-2 3 4-5 5z"/></svg></span>Full-service support / even if you’re abroad</li>
      <li class="why__item"><span class="why__icon"><svg viewBox="0 0 16 16"><rect x="2" y="3" width="12" height="11" rx="1"/><path d="M2 6.5h12M5 1.5v3M11 1.5v3"/></svg></span>7-day availability, including evening</li>
    </ul>
  </div>
</section>

<!-- Spanish side -->
<section class="flyer flyer--es" lang="es">
  <div class="hero">
    <div class="brand">
      <span class="brand__mark"></span>
      <div>
        <div class="brand__name">Golden Harbour</div>
        <div class="brand__areas">Marbella Estepona Sotogrande</div>
        <div class="brand__web">www.golden-harbour.example</div>
      </div>
    </div>
    <h1 class="headline" style="top:138px">
      <span class="headline__line" style="font-size:40px"><span class="tag tag--blue">Vende</span>&nbsp; <span class="c-blue">bien.</span></span>
      <span class="headline__line" style="font-size:40px"><span class="tag tag--yellow">Vende</span>&nbsp; <span class="c-yellow">ya.</span></span>
      <span class="headline__line" style="font-size:40px"><span class="tag tag--rust">Vende</span></span>
      <span class="headline__line" style="font-size:36px"><span class="c-rust" style="font-size:26px">con</span> <span class="c-rust">nosotros.</span></span>
    </h1>
    <div class="hero__rule" style="top:309px"></div>
    <p class="hero__cta" style="top:315px">¡Empecemos hoy mismo!</p>
  </div>

  <aside class="agent">
    <p class="agent__title">Tu especialista en<br>propiedades para<br>Estepona, Manilva y<br>Sotogrande.</p>
    <div class="agent__hello">Hola!</div>
    <div class="agent__photo" role="img" aria-label="Foto de retrato de la agente"></div>
    <p class="agent__contact">Lucia Marvel<br>(+34) 600 41 82 57<br><small>lucia@golden-harbour.example</small></p>
  </aside>

  <div class="photo photo--office" role="img" aria-label="Foto de la oficina de la agencia en una esquina"></div>
  <div class="photo photo--building" role="img" aria-label="Foto de un edificio blanco de apartamentos con piscina"></div>

  <h2 class="question">¿Vas a vender tu propiedad en la Costa del Sol?</h2>
  <div class="photo photo--pool" role="img" aria-label="Foto de un complejo residencial con piscina"></div>
  <div class="offer">
    <h3 class="offer__title">Lo hacemos<br>fácil, rápido<br>y rentable.</h3>
    <div class="offer__rule"></div>
    <p class="offer__contact">Llama al 951 000 742<br>sell@golden-harbour.example</p>
    <div class="offer__rule"></div>
    <p class="offer__text">Pasamos por tu propiedad, hacemos fotos profesionales y te damos una tasación gratuita, sin compromiso.</p>
  </div>

  <div class="why">
    <h2 class="why__title">¿Por qué vender<br>con nosotros?</h2>
    <ul class="why__list">
      <li class="why__item"><span class="why__icon"><svg viewBox="0 0 16 16"><rect x="1.5" y="4.5" width="13" height="9" rx="1.5"/><circle cx="8" cy="9" r="2.5"/><path d="M5.5 4.5l1-2h3l1 2"/></svg></span>Fotos impresionantes, tomas con dron y tours 360°</li>
      <li class="why__item"><span class="why__icon"><svg viewBox="0 0 16 16"><rect x="1.5" y="2.5" width="8" height="7" rx="1"/><rect x="6.5" y="6.5" width="8" height="7" rx="1"/></svg></span>Descripciones multilingües y máxima visibilidad</li>
      <li class="why__item"><span class="why__icon"><svg viewBox="0 0 16 16"><circle cx="7" cy="7" r="5"/><path d="M10.5 10.5l4 4"/><path d="M5 8V6.5l2-1.5 2 1.5V8z"/></svg></span>Publicada en más de 2,000 agencias y los principales portales</li>
      <li class="why__item"><span class="why__icon"><svg viewBox="0 0 16 16"><path d="M2 8l3-4 3 2 3-2 3 4-5 5z"/></svg></span>Soporte completo, incluso si estás en el extranjero</li>
      <li class="why__item"><span class="why__icon"><svg viewBox="0 0 16 16"><rect x="2" y="3" width="12" height="11" rx="1"/><path d="M2 6.5h12M5 1.5v3M11 1.5v3"/></svg></span>Disponibles 7 días a la semana, ¡también por la tarde!</li>
    </ul>
  </div>
</section>

</body>
</html>
```